Hollyfern Yuletide Firs needs words putting into pictures!

Hollyfern Yuletide Firs sells real Christmas Trees directly to consumers and retailers. A "growing" part of our business is fulfilling online orders e.g. a garden centre sells a tree online, and we do everything else from selecting the tree to delivery. We are now looking to market this service as best in class due to the selection process we have, and a link up we have made with a courier company.

We want to summarise the process into a simple one page graphic that illustrates the process from start to finish in simple language, short sentences, with images and pictures.

Given how difficult it is to get good images of Christmas trees, we thought simple outline pictures could work - almost like sketches. We are open to all ideas.

We can provide any of the images in the attached brochure, and many more depending what you may require.

We like clean cut, simple designs that are clear and innovative.

Contact Information for Business Card

Martin Crane, Director, Hollyfern Yuletide Firs, martin@hollyfernyuletidefirs.com, Brookside Meadow, Fenwick Road, Marbury Heath, LT4 9QD

Font styles to use
Sans Serif

Colors
00a990

Requirements
Must have
• Condense the info down into a manageable graphic that shows our customers clearly what service we are able to provide
Nice to have
• Simple, elegant design to compliment brand feel
Should not have
• Not be too complicated

```html
<!DOCTYPE html>
<html lang="en">
<head>
<meta charset="utf-8">
<title>Hollyfern Yuletide Firs – From Farm to Door</title>
<link rel="stylesheet" href="https://fonts.googleapis.com/css2?family=Great+Vibes&family=Montserrat:wght@400;700;800&display=swap">
<style>
  :root {
    --page: #eceae6;
    --card: #1d4e5f;
    --teal: #00a990;
    --teal-deep: #1a8f7e;
    --lime: #c8d23a;
    --yellow: #f0c419;
    --orange: #e8782a;
    --red: #d9482f;
    --body-copy: #8fb3b8;
    --star: #f3d23b;
  }
  * { margin: 0; padding: 0; box-sizing: border-box; }
  html, body { width: 1200px; height: 900px; overflow: hidden; background: var(--page); }
  body { position: relative; font-family: "Montserrat", sans-serif; }

  .flyer {
    position: absolute; left: 100px; top: 117px;
    width: 1000px; height: 667px;
    background: var(--card);
    overflow: hidden;
  }
  .flyer__top-band { position: absolute; left: 0; top: 0; width: 100%; height: 10px; background: var(--teal-deep); z-index: 2; }

  .headline__script {
    position: absolute; left: 74px; top: 44px;
    font-family: "Great Vibes", cursive; font-size: 120px; line-height: 1;
    font-weight: 400;
    color: var(--teal-deep); white-space: nowrap;
  }
  .headline__caps {
    position: absolute; left: 185px; top: 178px;
    font-family: "Montserrat", sans-serif; font-weight: 800; font-size: 60px;
    letter-spacing: 0.5px; line-height: 1; color: var(--red); white-space: nowrap;
  }

  .tree-flourish {
    position: absolute; left: 840px; top: 80px; width: 130px; height: 210px;
  }

  .graphics { position: absolute; left: 0; top: 0; width: 1000px; height: 667px; }

  .step { position: absolute; padding-left: 14px; }
  .step__bar { position: absolute; left: 0; top: 0; width: 4px; }
  .step__title { font-weight: 700; font-size: 16px; line-height: 1.2; margin-bottom: 10px; }
  .step__text { font-size: 13.5px; line-height: 1.25; color: var(--body-copy); }

  .step--planted { left: 140px; top: 268px; width: 170px; }
  .step--planted .step__bar { height: 64px; background: var(--lime); }
  .step--planted .step__title { color: var(--lime); }

  .step--selection { left: 318px; top: 268px; width: 300px; }
  .step--selection .step__bar { height: 80px; background: var(--yellow); }
  .step--selection .step__title { color: var(--yellow); }

  .step--pick { left: 490px; top: 502px; width: 160px; }
  .step--pick .step__bar { height: 84px; background: var(--orange); }
  .step--pick .step__title { color: var(--orange); }

  .step--delivery { left: 661px; top: 502px; width: 240px; }
  .step--delivery .step__bar { height: 84px; background: var(--red); }
  .step--delivery .step__title { color: var(--red); }

  .contact-band {
    position: absolute; left: 0; bottom: 0; width: 100%; height: 47px;
    background: var(--red);
    display: flex; align-items: center; justify-content: center; gap: 58px;
    font-weight: 700; font-size: 18px; color: var(--card);
  }
  .contact-band__divider { font-weight: 400; }
</style>
</head>
<body>
  <main class="flyer">
    <div class="flyer__top-band"></div>

    <h1 class="headline">
      <span class="headline__script">Hollyfern</span>
      <span class="headline__caps">YULETIDE FIRS</span>
    </h1>

    <div class="tree-flourish" role="img" aria-label="Swirling line drawing of a Christmas tree">
      <svg width="130" height="210" viewBox="0 0 130 210">
        <defs>
          <linearGradient id="flourishFill" x1="0" y1="0" x2="0" y2="1">
            <stop offset="0" stop-color="#1a8f7e" stop-opacity="0.15"/>
            <stop offset="1" stop-color="#1a8f7e" stop-opacity="0.55"/>
          </linearGradient>
        </defs>
        <polygon points="72,20 128,205 0,205" fill="url(#flourishFill)"/>
      </svg>
    </div>

    <svg class="graphics" viewBox="0 0 1000 667" aria-hidden="true">
      <polygon fill="var(--star)" points="877,40 882,53 896,54 885,63 889,77 877,69 865,77 869,63 858,54 872,53"/>

      <g stroke="var(--teal-deep)" stroke-width="11" fill="none">
        <line x1="168" y1="512" x2="198" y2="510"/>
        <line x1="232" y1="505" x2="272" y2="500"/>
        <line x1="388" y1="463" x2="412" y2="457"/>
        <line x1="543" y1="432" x2="577" y2="417"/>
        <line x1="612" y1="401" x2="635" y2="392"/>
        <line x1="716" y1="333" x2="790" y2="280"/>
      </g>
      <polygon fill="var(--teal-deep)" points="812,262 778,268 797,294"/>

      <g stroke="var(--body-copy)" stroke-width="1.5" stroke-dasharray="2 4">
        <line x1="142" y1="338" x2="142" y2="440"/>
        <line x1="320" y1="352" x2="320" y2="412"/>
        <line x1="663" y1="446" x2="663" y2="496"/>
      </g>

      <g stroke="var(--lime)" stroke-width="3" fill="none">
        <path d="M128 506 v12 a14 14 0 0 0 28 0 v-12 z"/>
        <line x1="142" y1="476" x2="142" y2="518"/>
      </g>
      <rect x="126" y="452" width="32" height="34" rx="14" fill="var(--lime)" opacity="0.85" role="img" aria-label="Seedling leaves"/>

      <circle cx="328" cy="482" r="40" fill="none" stroke="var(--lime)" stroke-width="4"/>
      <polygon points="328,458 346,500 310,500" fill="none" stroke="var(--lime)" stroke-width="2.5"/>
      <line x1="300" y1="514" x2="286" y2="530" stroke="var(--orange)" stroke-width="9" stroke-linecap="round"/>

      <rect x="430" y="345" width="100" height="125" rx="8" fill="var(--lime)" opacity="0.22" role="img" aria-label="Outline of a hand pointing at two small trees"/>

      <g fill="var(--lime)">
        <rect x="636" y="364" width="60" height="22"/>
        <path d="M696 366 h22 l14 12 v8 h-36 z"/>
        <circle cx="652" cy="390" r="6" stroke="var(--card)" stroke-width="2"/>
        <circle cx="718" cy="390" r="6" stroke="var(--card)" stroke-width="2"/>
      </g>
      <text x="640" y="373" font-family="Montserrat, sans-serif" font-weight="800" font-size="7.5" fill="var(--card)">SPECIAL</text>
      <text x="640" y="382" font-family="Montserrat, sans-serif" font-weight="700" font-size="7.5" fill="var(--card)">DELIVERY</text>
    </svg>

    <section class="step step--planted">
      <span class="step__bar"></span>
      <h2 class="step__title">Planted with love</h2>
      <p class="step__text">Our trees are carefully planted in our Scotish farms</p>
    </section>

    <section class="step step--selection">
      <span class="step__bar"></span>
      <h2 class="step__title">Creful selection</h2>
      <p class="step__text">Our trees go through a careful selection<br>to ensure maximum freshness.</p>
    </section>

    <section class="step step--pick">
      <span class="step__bar"></span>
      <h2 class="step__title">Customer pick</h2>
      <p class="step__text">Our customers pick<br>their own tree</p>
    </section>

    <section class="step step--delivery">
      <span class="step__bar"></span>
      <h2 class="step__title">Special delivery</h2>
      <p class="step__text">The tree is delivered to you by<br>our special delivery service</p>
    </section>

    <footer class="contact-band">
      <span class="contact-band__phone">+44 (0)1632 960418</span>
      <span class="contact-band__divider">|</span>
      <span class="contact-band__email">sales@hollyfernyuletidefirs.com</span>
    </footer>
  </main>
</body>
</html>
```